Brenvik Auto Logo Design

Brenvik Auto Sales & Service is a automotive repair shop and car dealership. We specialize in Norvane & Kestrelwerk, so we would like our cards to let our customers know that we are a German import specialist and that we are QTR certified. We are looking for something that is sharp, with clean lines, and very professional. We specialize in Norvane and Kestrelwerk, so we want to appeal to the higher end customer. We want a business card that will do so. Please no cars, tires or tools on the logo. We want this to look tactful and professional. We would also like our link to our facebook page included on the business card. https://www.examplesocial.test/brenvikautosalesservice

Industry/Entity Type

Automotive

Contact Information for Business Card

Brenvik Auto Sales & Service
Doug & Melinda Brenvik
482 E Thornbury Avenue
PO Box 63
Kellsford, ND 54911
Phone 555-555-0187
Fax 555-555-0193

Logo Text

```html
<!DOCTYPE html>
<html lang="en">
<head>
<meta charset="utf-8">
<title>Brenvik Auto – Logo and Business Card</title>
<link href="https://fonts.googleapis.com/css2?family=Arimo:ital,wght@0,400;0,700;1,400;1,700&display=swap" rel="stylesheet">
<style>
  :root {
    --brand-blue: #476788;
    --brand-yellow: #e5d22e;
    --paper: #ffffff;
  }
  html, body {
    margin: 0;
    padding: 0;
    width: 1200px;
    height: 960px;
    overflow: hidden;
    background: var(--paper);
    font-family: "Arimo", Arial, sans-serif;
  }
  .canvas {
    position: relative;
    width: 1200px;
    height: 960px;
  }
  .logo-band {
    position: absolute;
    left: 0;
    top: 0;
    width: 1200px;
    height: 333px;
    background: var(--brand-blue);
    display: flex;
    align-items: center;
    justify-content: center;
  }
  .wordmark {
    color: var(--brand-yellow);
    font-weight: 700;
    letter-spacing: 2px;
    white-space: nowrap;
    margin: 0;
  }
  .logo-band .wordmark {
    font-size: 64px;
    transform: translateX(-34px);
  }
  .business-card {
    position: absolute;
    left: 251px;
    top: 437px;
    width: 761px;
    height: 426px;
  }
  .card-shape {
    position: absolute;
    inset: 0;
  }
  .card-logo {
    position: absolute;
    left: 0;
    top: 0;
    width: 316px;
    height: 426px;
    display: flex;
    align-items: center;
    justify-content: center;
  }
  .card-logo .wordmark {
    font-size: 38px;
    letter-spacing: 1px;
  }
  .card-details {
    position: absolute;
    inset: 0;
    color: var(--brand-blue);
  }
  .contact-name {
    position: absolute;
    left: 403px;
    top: 75px;
    margin: 0;
    font-size: 25px;
    font-weight: 700;
    font-style: italic;
    white-space: nowrap;
  }
  .contact-title {
    position: absolute;
    left: 403px;
    top: 116px;
    margin: 0;
    font-size: 22px;
    font-style: italic;
  }
  .address {
    position: absolute;
    left: 489px;
    top: 188px;
    margin: 0;
    font-style: normal;
    font-size: 22px;
    line-height: 34px;
    white-space: nowrap;
  }
  .phones {
    position: absolute;
    left: 489px;
    top: 306px;
    margin: 0;
    padding: 0;
    list-style: none;
    font-size: 22px;
    font-style: italic;
    line-height: 37px;
    white-space: nowrap;
  }
</style>
</head>
<body>
<main class="canvas">
  <section class="logo-band">
    <p class="wordmark">Brenvik Auto</p>
  </section>

  <section class="business-card">
    <svg class="card-shape" width="761" height="426" viewBox="0 0 761 426">
      <rect x="0.75" y="0.75" width="759.5" height="424.5" fill="var(--paper)" stroke="var(--brand-blue)" stroke-width="1.5"/>
      <path d="M0 0 H424 C360 55 320 130 320 213 C320 295 355 365 414 426 H0 Z" fill="var(--brand-blue)"/>
    </svg>
    <div class="card-logo">
      <p class="wordmark">Brenvik Auto</p>
    </div>
    <div class="card-details">
      <h1 class="contact-name">Doug &amp; Melinda Brenvik</h1>
      <p class="contact-title">Title</p>
      <address class="address">
        482 E Thornbury Avenue<br>
        PO Box 63<br>
        Kellsford, ND 54911
      </address>
      <ul class="phones">
        <li>P : 555-555-0187</li>
        <li>F : 555-555-0193</li>
      </ul>
    </div>
  </section>
</main>
</body>
</html>
```